Meadow Healers WEBSITE
Meadow Healers WEBSITE - Health
Creative Brief
Health
www.meadowhealers.example
This website will be used by medical doctors mainly in the United States and some from other parts of the world. These doctors all have lots of research and many years of experience with patients. We have a team of people writing a book and we want about 600 doctors to fill out a questionaire and write about their research for this book. They will be going to this website to learn about us, what we are doing, why it is important for them to be included in this book and then they will decide if they want to fill out the questionaires and upload their literature and their research to us. We need for them to watch a video . There will be a 4 minute video embedded for the front page and the content will be word press. You will receive this next week. Your development team will upload the video we will make. The doctors will send their info to our email address and they MUST agree to a "terms and conditions" or we will not accept their content. We will give each doctor the SAME password to use. They must fill out their name and email address in full in order for us to receive the information they send.
It needs to be simple yet modern and exciting. So yes, you can use for the places to click onto modern and fun styles. Whether it is carrots or asparagus or avocados or broccoli or beans or other vegetables that flash or outline a location move or whatever you come up with.. sure I am open to that. I just need a little more than any other website design. I want these doctors to fall in love with the professional website and of course the content and really want to be a part of this team and agree to be a part of this book they all deserve to be in. I want you to use all the photos I have uploaded. The "notebook photo" will go where the questionaire form is for them to fill out.
Modern
Soft Pale Green ... peaceful to the eyes
Soft Pale Blue peaceful to the eyes
Soft yellow, grey or magenta
top
www.brambletidecare.example
http://fernloftkitchen.example/
I put brambletidecare.example ONLY because I like the background of rich deep forest and the colors. If you think we it would look good to have fruits and vegetables as the background or border, then let me know if I should be sending you a photo or find one to use for now and get my opinion. Then the inside would be very very soft pale colors... pale lime green for example, pale magenta. Also I only referred to the website fernloftkitchen because I like the moderness of it and I like how the top words do NOT have boxes around them. But the letters are tooooo small. The grey is modern and interesting, but if we use grey it must be A LOT lighter and soft. I need for the doctors to be able to access the questions only with a password. We will have a link at the top that says Doctors Questionaire. They must be able to fill part of it out, save it and be able to return to the forms without losing all the data they put onto the questionaire. We need about 6 links at the top. I want the video for them to watch to be in the center or on the right side. Whatever you think looks best. The links at the top will say who we are, What we want to accomplish, What this book is about Why it is important you be a part of this well respected team ( I realize these are long, however we can shorten the phrases... maybe) and we will add a couple of more. You will see the logo. PLEASE make that BIG and at the top. ALSO, we have ANOTHER logo which is different that I will ALSO be using. I will upload the 2nd logo and the video next week. In the meantime please work only with the logo you have now. I have 2 fun logos to use for this website. PLEASE put the links that are at the top also on the bottom of the page too. When doctors click on to different pages I want to have these beautiful photos everywhere. You will see a photo with a little baby and LOTS of vegetables. Put that at the top of the page. Then a beautiful African American girl with food. Please put that also on the front page and ONE OTHER that has a doctor with food. Please put all of those on the front page and big. Thank you!! Meadow Healers WEBSITE

```html
<!DOCTYPE html>
<html lang="en">
<head>
<meta charset="utf-8">
<title>Meadow Healers</title>
<link href="https://fonts.googleapis.com/css2?family=Arimo:wght@400;700&display=swap" rel="stylesheet">
<style>
:root{
  --green:#7ab51d;
  --green-dark:#5d8f12;
  --purple:#8b2a86;
  --text:#3c3c3c;
  --muted:#7a7a7a;
  --line:#d9dfd0;
  --white:#ffffff;
}
*{box-sizing:border-box;margin:0;padding:0}
html,body{width:1200px;height:1037px;overflow:hidden}
body{font-family:"Arimo",Arial,sans-serif;color:var(--text);
  background:radial-gradient(ellipse 560px 620px at 600px 520px,#ffffff 55%,#f2f8e6 75%,#d9ebbd 100%);
  position:relative}
.edge{position:absolute;top:0;height:1037px;width:175px}
.edge-left{left:0;background:linear-gradient(90deg,#cfe5a6,#eef6e0 80%,rgba(255,255,255,0))}
.edge-right{right:0;background:linear-gradient(270deg,#d6e9b2,#f0f7e4 80%,rgba(255,255,255,0))}
.abs{position:absolute}

.brand{left:175px;top:30px;display:flex;align-items:center;gap:12px}
.brand-dot{width:40px;height:40px;border-radius:50%;background:var(--green)}
.brand-name{font-size:34px;font-weight:700;color:var(--green);letter-spacing:.5px;white-space:nowrap}

.contact{left:560px;top:30px;width:328px;text-align:right;white-space:nowrap}
.contact-phone{font-size:19px;font-weight:700;color:var(--text)}
.contact-phone span{color:var(--purple)}
.contact-mail{position:absolute;right:76px;top:26px;font-size:12px;color:var(--text)}
.contact-mail span{color:var(--purple)}
.login{left:822px;top:52px;width:52px;height:20px;background:var(--green);color:#fff;font-size:10px;font-weight:700;display:flex;align-items:center;justify-content:center;border-radius:2px}
.social{left:894px;top:32px;display:flex;gap:6px}
.social span{width:28px;height:28px;border-radius:50%;background:#4aa3df}
.social span:nth-child(2){background:#3b5a9a}
.social span:nth-child(3){background:#1b7ab6}
.social span:nth-child(4){background:#f08a24}

.nav{left:478px;top:110px;width:547px;height:30px;display:flex;align-items:center;justify-content:space-between;border-bottom:1px solid var(--line)}
.nav a{font-size:9px;font-weight:700;color:var(--text);text-decoration:none;padding:10px 3px;white-space:nowrap}
.nav a.active{background:var(--green);color:#fff;padding:10px 10px}

.welcome{left:225px;top:198px;width:290px}
.welcome h1{font-size:28px;font-weight:400;color:var(--text)}
.welcome .brand-small{font-size:24px;font-weight:700;color:var(--green);margin:8px 0 18px}
.welcome p{font-size:13.5px;line-height:1.45;color:var(--text);margin-bottom:16px}

.video{left:534px;top:155px;width:491px;height:280px;border:4px solid #fff;box-shadow:0 0 6px rgba(0,0,0,.25);
  background:linear-gradient(135deg,#e6f1fb,#b7d2ec 45%,#e7a892 50%,#b7d2ec 56%,#dcebf8)}
.video .play{position:absolute;left:215px;top:110px;width:54px;height:54px;border-radius:6px;background:rgba(30,30,30,.75)}

.features{left:175px;top:452px;width:850px;height:150px;background:#fff;border:1px solid var(--line);display:flex;box-shadow:0 1px 4px rgba(0,0,0,.08)}
.feature{width:144px;padding:10px 12px;border-right:1px solid var(--line)}
.feature h3{font-size:15px;font-weight:700;color:var(--text);margin-bottom:6px}
.feature p{font-size:11px;line-height:1.35;color:var(--muted)}
.feature .more{display:inline-block;margin-top:6px;font-size:11px;font-weight:700;color:var(--green)}
.thumb{width:133px;height:128px;margin:10px 0 0 6px;border:1px solid var(--line)}
.thumb-baby{background:linear-gradient(180deg,#f4ede4,#e7d8c4 55%,#8fbf4c)}
.thumb-girl{background:linear-gradient(180deg,#c9e39b,#7a4e33 45%,#e09a3c)}
.thumb-woman{background:linear-gradient(180deg,#f3f3f3,#c98e63 50%,#d8452c)}

.doctor-photo{left:175px;top:624px;width:185px;height:211px;background:linear-gradient(180deg,#eeeeee,#d8b49a 45%,#f2f2f2 70%,#6aa632)}
.accomplish{left:374px;top:624px;width:305px}
.accomplish h2{font-size:17px;font-weight:700;color:var(--text);margin-bottom:10px}
.accomplish p{font-size:11px;line-height:1.4;color:var(--muted);margin-bottom:8px}
.accomplish .link{color:var(--green);font-weight:700}
.group-photo{left:697px;top:624px;width:303px;height:135px;background:linear-gradient(180deg,#bfe0f5,#cfe6a8 40%,#a96e48 70%,#64a12e)}
.newsletter{left:697px;top:768px;width:303px}
.newsletter h2{font-size:22px;font-weight:700;color:var(--purple)}
.newsletter p{font-size:10px;color:var(--muted);margin:2px 0 8px}
.newsletter .field{display:flex}
.newsletter .input{width:223px;height:22px;border:1px solid #cfcfcf;background:#fff;font-size:10px;color:#999;padding:5px 6px}
.newsletter .btn{width:80px;height:22px;background:var(--green);color:#fff;font-size:10px;font-weight:700;display:flex;align-items:center;justify-content:center}

.swoosh{left:175px;top:852px}
.veg-row{left:490px;top:858px;width:230px;height:40px;border-radius:20px 20px 4px 4px;background:linear-gradient(90deg,#6aa82e,#d9462a 30%,#f2a23a 55%,#4f8f24 80%,#8a3a7c)}

.footer-nav{left:175px;top:969px;display:flex;gap:12px}
.footer-nav a{font-size:9.5px;color:var(--text);text-decoration:none}
.copyright{left:175px;top:990px;font-size:9px;color:var(--muted)}
.copyright span{color:var(--purple)}
.footer-brand{left:860px;top:966px;display:flex;align-items:center;gap:8px}
.footer-brand .brand-dot{width:28px;height:28px}
.footer-brand .brand-name{font-size:22px}
</style>
</head>
<body>
<div class="edge edge-left" role="img" aria-label="Soft-focus fresh fruits and vegetables along the left edge"></div>
<div class="edge edge-right" role="img" aria-label="Soft-focus fresh fruits and vegetables along the right edge"></div>

<header>
  <div class="abs brand"><span class="brand-dot"></span><span class="brand-name">Meadow Healers</span></div>
  <div class="abs contact">
    <div class="contact-phone">Contact Us: <span>555.014.2286</span></div>
    <div class="contact-mail">Email: <span>meadowhealers.example</span></div>
  </div>
  <div class="abs login">LOGIN</div>
  <div class="abs social"><span></span><span></span><span></span><span></span></div>
  <nav class="abs nav">
    <a class="active" href="#">HOME</a>
    <a href="#">WHO WE ARE</a>
    <a href="#">WHAT WE WANT TO ACCOMPLISH</a>
    <a href="#">WHAT THIS BOOK IS ABOUT</a>
    <a href="#">WHY IT IS IMPORTANT</a>
  </nav>
</header>

<section class="abs welcome">
  <h1>Welcome to</h1>
  <div class="brand-small">Meadow Healers</div>
  <p>This website will be used by medical doctors mainly in the United States and some from other parts of the world.</p>
  <p>These doctors all have lots of research and many years of experience with patients.</p>
</section>

<div class="abs video" role="img" aria-label="Video preview: medical illustration of a heart with a heartbeat trace">
  <div class="play"><svg width="54" height="54" viewBox="0 0 54 54"><polygon points="21,16 21,38 38,27" fill="#fff"/></svg></div>
</div>

<section class="abs features">
  <div class="feature"><h3>Who We Are</h3><p>Sed ut perspiciatis unde omnis iste natus error sit voluptatem accusantium dolore.</p><span class="more">Read More</span></div>
  <div class="feature"><h3>What This Book is About</h3><p>Sed ut perspiciatis unde omnis iste natus error sit voluptatem.</p><span class="more">Read More</span></div>
  <div class="feature"><h3>Why It Is Important</h3><p>Sed ut perspiciatis unde omnis iste natus error sit voluptatem.</p><span class="more">Read More</span></div>
  <div class="thumb thumb-baby" role="img" aria-label="Photo of a baby surrounded by vegetables"></div>
  <div class="thumb thumb-girl" role="img" aria-label="Photo of a smiling girl with a bowl of vegetables"></div>
  <div class="thumb thumb-woman" role="img" aria-label="Photo of a woman eating fresh produce"></div>
</section>

<div class="abs doctor-photo" role="img" aria-label="Photo of a doctor holding vegetables"></div>
<section class="abs accomplish">
  <h2>What We Want To Accomplish</h2>
  <p>Sed ut perspiciatis unde omnis iste natus error sit voluptatem accusantium doloremque laudantium, totam rem aperiam, eaque ipsa quae ab illo inventore veritatis et quasi architecto beatae vitae dicta sunt explicabo.</p>
  <p>Sed ut perspiciatis unde omnis iste natus error sit voluptatem accusantium doloremque laudantium, totam rem aperiam, eaque ipsa quae ab illo inventore veritatis et quasi architecto beatae vitae dicta sunt explicabo. Sed quia consequuntur magni dolores <span class="link">Neque porro quisquam est.</span></p>
</section>
<div class="abs group-photo" role="img" aria-label="Photo of children outdoors holding vegetables"></div>
<section class="abs newsletter">
  <h2>NEWSLETTER SIGNUP</h2>
  <p>Subscribe to our mailing list</p>
  <div class="field"><div class="input">Email address</div><div class="btn">SUBSCRIBE</div></div>
</section>

<svg class="abs swoosh" width="850" height="95" viewBox="0 0 850 95">
  <path d="M0 20 Q425 70 850 20 L850 55 Q425 95 0 55 Z" fill="#8b2a86"/>
  <path d="M0 10 Q425 60 850 10 L850 30 Q425 78 0 30 Z" fill="#7ab51d"/>
</svg>
<div class="abs veg-row" role="img" aria-label="Row of assorted fresh vegetables"></div>

<footer>
  <nav class="abs footer-nav">
    <a href="#">Home</a><a href="#">Who we are</a><a href="#">What we want to accomplish</a><a href="#">What this book is about</a><a href="#">Why it is important</a>
  </nav>
  <div class="abs copyright">Copyright © meadowhealers.example. All Rights Reserved. | <span>Privacy Policy</span></div>
  <div class="abs footer-brand"><span class="brand-dot"></span><span class="brand-name">Meadow Healers</span></div>
</footer>
</body>
</html>
```